Verpackungsdesign für Produkt gesucht
Zielgruppe
DE
Handelsunternehmen, weltweiter Vertrieb von unterschiedlichen Produkten unter eigenen Marken.
Neue internationale (Deutschland, EU) Marke in dem Segment Raucherprodukte.
Zielgruppe: Raucher
EN
Trading company, worldwide distribution of various products under own brands.
New international (Germany, EU) brand in the smoker products segment.
Target group: smokers
Aufgabenstellung
PRODUKT
- Markenname ist: brivt
- In diesem Fall benötigen wir ein Verpackungsdesign für das erste Produkt aus einer Reihe von
noch folgenden Produkten/Artikeln für Raucher.
Es besteht somit noch kein Markenbild oder andere Designs.
- Bei dem Produkt handelt es sich um einen durchsichtigen, ca. 2 cm langen Aufsteckfilter für
Zigaretten. Er wird auf eine Zigarette ohne Filter oder auf den eigentlichen Filter der Zigarette
gesteckt.
Der Filter ist durchsichtig konzipiert, damit man den gefilterten Schadstoffrückstand im Filter
sehen kann.
- Das Verpackungsdesign sollte clean und modern sein, für Mann und Frau.
- Verkauf über das Internet europaweit.
VERPACKUNG
Eine Idee für die Verpackungsform besteht bereits, jedoch sind auch offen für andere Vorschläge. Zur Orientierung bitte den Anhang ansehen! Dort haben wir Fotos hochgeladen, die ein Verpackungsmuster mit dem Produkt zeigen. Das Produkt im Bild hat einen gelben Filtereinsatz, unser Produkt wird jedoch einen orangefarbenen Filtereinsatz haben.
Bei der Verpackung handelt es sich um zwei Teile und beide sollen aus Karton sein:
1. Die Verpackung/Einzelpackung mit 50 Filtern Inhalt für das Produkt selbst
2. Eine Verpackung für fünf Einzelpackungen
Bei der Verpackung soll berücksichtigt werden, dass auf ihm ein Piktogramm mit Text auf der Vorderseite untergebracht werden muss, welches in verschiedenen Sprachen darauf hinweißt, dass Kunststoff nicht achtlos in die Umwelt entsorgt wird. Dieses Piktrogramm muss 6% der Fläche (Vorderseite auf der es gedruckt ist) einnehmen. Desweiteren muss ein Barcode angebracht werden. Beides ist ebenfalls im Anhang zu finden.
Was benötigen wir von Ihnen?
- Wir benötigen ein Design für beide Teile der Verpackung, natürlich soll auch der Markenname (brivt) auf der Verpackung ein schönes und modernes Design erhalten.

```html
<!DOCTYPE html>
<html lang="de">
<head>
<meta charset="utf-8">
<title>brivt Aufsteckfilter – Verpackung</title>
<link rel="stylesheet" href="https://fonts.googleapis.com/css2?family=Questrial&family=Archivo+Black&display=swap">
<style>
  :root {
    --bg: #d9d8d4;
    --paper: #f7f7ee;
    --lime: #e1e03d;
    --ink: #3a3838;
    --black: #111111;
    --warn-red: #e52b48;
    --warn-blue: #5cc3ee;
    --white: #ffffff;
  }
  * { margin: 0; padding: 0; box-sizing: border-box; }
  html, body { width: 905px; height: 1200px; overflow: hidden; }
  body { background: var(--bg); position: relative; font-family: "Questrial", sans-serif; color: var(--ink); }

  .panel { position: absolute; left: 50px; width: 805px; background: var(--paper); overflow: hidden; }
  .panel-top { top: 150px; height: 620px; }
  .panel-side { top: 790px; height: 180px; }
  .panel .sweep { position: absolute; inset: 0; width: 100%; height: 100%; }

  .brand-name { position: absolute; font-family: "Questrial", sans-serif; color: var(--ink); line-height: 1; letter-spacing: -0.02em; white-space: nowrap; }
  .product-type { position: absolute; font-family: "Questrial", sans-serif; color: var(--ink); letter-spacing: 0.38em; line-height: 1; white-space: nowrap; }

  .panel-top .brand-name { left: 80px; top: 40px; font-size: 180px; }
  .panel-top .product-type { left: 90px; top: 255px; font-size: 32px; }

  .count { position: absolute; left: 40px; bottom: 28px; font-family: "Archivo Black", sans-serif; font-size: 56px; color: var(--ink); line-height: 1; }

  .warning-text { position: absolute; left: 290px; top: 462px; font-family: "Archivo Black", sans-serif; font-size: 9px; line-height: 1.3; letter-spacing: 0.06em; color: var(--black); text-transform: uppercase; white-space: nowrap; }

  .pictogram { position: absolute; left: 488px; top: 452px; width: 290px; height: 140px; border: 3px solid var(--black); background: var(--white); display: flex; flex-direction: column; }
  .pictogram-icons { flex: 1; display: flex; }
  .pictogram-icons .icon-field { flex: 1; }
  .icon-no-littering { background: var(--warn-red); }
  .icon-ocean { background: var(--warn-blue); }
  .pictogram-caption { height: 30px; display: flex; align-items: center; justify-content: center; font-family: "Archivo Black", sans-serif; font-size: 14px; letter-spacing: 0.03em; color: var(--black); background: var(--white); white-space: nowrap; }

  .panel-side .brand-name { left: 40px; top: 18px; font-size: 92px; }
  .panel-side .product-type { left: 44px; top: 128px; font-size: 16px; }
  .dispense-slot { position: absolute; left: 330px; top: 54px; width: 110px; height: 72px; background: var(--black); border-radius: 3px; }
</style>
</head>
<body>

  <section class="panel panel-top">
    <svg class="sweep" viewBox="0 0 805 620" preserveAspectRatio="none" aria-hidden="true">
      <path d="M805 0 L790 0 C620 260 430 520 250 620 L805 620 Z" fill="var(--lime)"/>
    </svg>
    <div class="brand-name">brivt</div>
    <div class="product-type">AUFSTECKFILTER</div>
    <div class="count">50</div>

    <div class="warning-text">
      Plastic in filter<br>
      Filtre contenant<br>
      du plastique<br>
      Plastica nel filtro<br>
      Filter bevat plastic<br>
      Filtret innehaller plasta
    </div>

    <div class="pictogram">
      <div class="pictogram-icons">
        <div class="icon-field icon-no-littering" role="img" aria-label="Piktogramm: Zigarette nicht wegwerfen"></div>
        <div class="icon-field icon-ocean" role="img" aria-label="Piktogramm: Kunststoffmüll im Meer mit Schildkröte"></div>
      </div>
      <div class="pictogram-caption">FILTER ENTHÄLT KUNSTSTOFF</div>
    </div>
  </section>

  <section class="panel panel-side">
    <svg class="sweep" viewBox="0 0 805 180" preserveAspectRatio="none" aria-hidden="true">
      <path d="M805 0 L330 0 C300 60 260 130 210 180 L805 180 Z" fill="var(--lime)"/>
    </svg>
    <div class="brand-name">brivt</div>
    <div class="product-type">AUFSTECKFILTER</div>
    <div class="dispense-slot"></div>
  </section>

</body>
</html>
```